need professional, precise design for a website

I will start with a homepage design and if we pick your design, we'll have you design up to 6 more interior pages (we'll pay extra for these of course). We need a homepage design for a reserve study company based in Idaho, covering the northwest region. The company is called copper ridge capital study. Their current site is at https://www.copperridgecapital.example/ and they really like this site for inspiration https://www.fundplanhub.example/ but they would like an original design, just more modern and fresh like the sample site. I have logo files I will attach. They want something that looks financial and has a feel of accuity. Their main call to action will be to have someone fill in a contact form or call them on the phone. They will have a sample study that someone can download as on the fundplanhub site. You can use copy from their current site.

```html
<!DOCTYPE html>
<html lang="en">
<head>
<meta charset="utf-8">
<title>Copper Ridge Capital – Reserve Studies</title>
<link href="https://fonts.googleapis.com/css2?family=Roboto:wght@300;400;500;700;900&display=swap" rel="stylesheet">
<style>
:root{
  --navy:#1c2566;
  --deep:#123f78;
  --sky:#0eaaea;
  --cyan:#14b4f0;
  --green:#1aaa4a;
  --orange:#ec6d36;
  --steel:#3a7bbf;
  --mist:#eef6fa;
  --ink:#444;
  --grey:#d2d3d5;
  --white:#fff;
}
*{margin:0;padding:0;box-sizing:border-box}
html,body{width:775px;height:1200px;overflow:hidden}
body{font-family:'Roboto',sans-serif;background:var(--white);position:relative}
.abs{position:absolute}

/* header */
.site-header{left:0;top:0;width:775px;height:59px;background:var(--white)}
.brand{left:88px;top:28px;display:flex;align-items:center;gap:6px;color:var(--navy);font-size:14px;font-weight:400;letter-spacing:.3px}
.brand-dot{width:12px;height:12px;border-radius:50%;background:var(--navy)}
.main-nav{left:434px;top:36px;display:flex;gap:38px;font-size:8.5px;color:#555;letter-spacing:.2px}
.main-nav .caret{font-size:6px;margin-left:3px}

/* hero (children positioned relative to the hero box) */
.hero{left:0;top:59px;width:775px;height:293px;background:linear-gradient(90deg,#dcd6cc 0%,#d8d4cb 30%,#3c8fd0 50%,#1e7fcf 70%,#1b74c4 100%);overflow:hidden}
.hero-map{left:0;top:0;width:420px;height:293px;background:linear-gradient(135deg,#e4ddd2 0%,#d9d4c9 45%,rgba(40,130,205,.9) 100%)}
.hero-title{left:340px;top:46px;width:360px;text-align:center;color:var(--navy);font-weight:700;font-size:30px;line-height:37px;letter-spacing:.3px}
.hero-title .big-line{display:flex;justify-content:center;align-items:center;gap:10px;margin-top:-4px}
.hero-title .thirty{font-size:88px;font-weight:900;line-height:82px}
.hero-title .small{font-size:27px}
.hero-call{left:580px;top:216px;color:var(--white);font-weight:700;font-size:17.5px;white-space:nowrap}
.hero-btn{left:580px;top:247px;width:164px;height:31px;background:var(--cyan);border-radius:3px;color:var(--white);font-size:13.5px;display:flex;align-items:center;justify-content:center;box-shadow:0 2px 4px rgba(0,0,0,.25)}

/* stats */
.stat-num{font-weight:700;line-height:1}
.stat-label{font-weight:500;font-size:13.5px;line-height:17px}
.divider{width:1px;height:84px;background:var(--steel);top:393px}

/* services */
.services{left:0;top:509px;width:775px;height:361px;background:var(--mist)}
.service-photo{top:43px;width:180px;height:103px}
.service-title{top:163px;color:#19a6e0;font-size:9.5px;line-height:11px;font-weight:400}
.service-text{top:196px;width:180px;color:var(--ink);font-size:7px;line-height:9.3px}
.more-btn{top:280px;width:67px;height:17px;background:var(--deep);border-radius:8px;color:var(--white);font-size:7px;font-weight:700;display:flex;align-items:center;justify-content:center}

/* call back */
.callback{left:0;top:870px;width:775px;height:161px;background:var(--deep)}
.callback-title{left:91px;top:54px;color:var(--white);font-size:13px;font-weight:700}
.callback-text{left:91px;top:75px;width:145px;color:#d9e3f0;font-size:6px;line-height:7.6px;font-weight:500}
.field{width:157px;height:22px;background:var(--cyan);color:var(--white);font-size:7px;font-weight:500;padding-left:11px;display:flex;align-items:center}
.field .arrow{margin-left:auto;margin-right:7px;font-size:5px}
.submit{left:622px;top:68px;width:77px;height:29px;background:#1eb554;color:var(--white);font-size:8px;font-weight:700;display:flex;align-items:center;justify-content:center;gap:6px}

/* footer */
.site-footer{left:0;top:1031px;width:775px;height:140px;background:var(--sky)}
.footer-brand{left:104px;top:26px;display:flex;align-items:center;gap:5px;color:var(--navy);font-size:10.5px}
.footer-brand .brand-dot{width:10px;height:10px}
.footer-info{left:107px;top:58px;color:#1c3f6e;font-size:7px;line-height:12.6px;font-weight:300}
.footer-nav{left:528px;top:42px;color:#2f7fb6;font-size:8px;line-height:21.5px;font-weight:300}
.social{left:528px;top:102px;display:flex;gap:14px}
.social span{width:11px;height:11px;border-radius:50%;background:#2f6aa0}
.copyright{left:0;top:1171px;width:775px;height:29px;background:var(--grey);color:#333;font-size:7px;display:flex;align-items:center;justify-content:center}
</style>
</head>
<body>

<header class="site-header abs">
  <div class="brand abs"><span class="brand-dot"></span>Copper Ridge Capital</div>
  <nav class="main-nav abs">
    <span>WHO WE ARE</span>
    <span>RESERVE STUDIES<span class="caret">▼</span></span>
    <span>CONTACT</span>
  </nav>
</header>

<section class="hero abs">
  <div class="hero-map abs" role="img" aria-label="Stylised city street map with location pins fading into blue"></div>
  <h1 class="hero-title abs">
    YOUR FINANCIAL ROAD<br>MAP FOR THE
    <span class="big-line"><span class="small">NEXT</span><span class="thirty">30</span><span class="small">YEARS!</span></span>
  </h1>
  <div class="hero-call abs">CALL (208) 555-0142</div>
  <div class="hero-btn abs">QUCK CONTACT</div>
</section>

<section class="stats">
  <div class="abs stat-num" style="left:172px;top:385px;font-size:56px;color:var(--green)">50</div>
  <div class="abs stat-label" style="left:179px;top:446px;color:var(--green)">CITIES<br>SERVED</div>
  <div class="divider abs" style="left:288px"></div>
  <div class="abs stat-num" style="left:323px;top:385px;font-size:56px;color:var(--orange)">100+</div>
  <div class="abs stat-label" style="left:331px;top:447px;font-size:12.5px;line-height:15px;color:var(--orange)">PROJECT<br>ENGAGEMENTS</div>
  <div class="divider abs" style="left:493px"></div>
  <div class="abs stat-num" style="left:520px;top:392px;font-size:56px;color:var(--steel)">20+</div>
  <div class="abs stat-label" style="left:522px;top:460px;font-size:12.5px;color:var(--steel)">EXPERIENCE</div>
</section>

<section class="services abs">
  <div class="service-photo abs" style="left:88px;background:linear-gradient(180deg,#7ea6c4 0%,#a3765b 45%,#8a8f6e 100%)" role="img" aria-label="Row of brick townhouses"></div>
  <div class="service-photo abs" style="left:301px;background:linear-gradient(180deg,#9aa6b0 0%,#7a3a30 40%,#4a2a28 100%)" role="img" aria-label="Glass and brick commercial building"></div>
  <div class="service-photo abs" style="left:513px;background:linear-gradient(180deg,#cfe0c8 0%,#3f6a2c 45%,#5f9a3a 100%)" role="img" aria-label="Park with trees, lawn and playground"></div>

  <div class="service-title abs" style="left:89px">HOA &amp;<br>CONDOMINIUM STUDIES</div>
  <div class="service-title abs" style="left:302px;font-size:8.5px">COMMERCIAL, VACATION &amp;<br>TIME SHARE</div>
  <div class="service-title abs" style="left:516px;font-size:8.5px">PARKS &amp;<br>PUBLIC LANDS</div>

  <p class="service-text abs" style="left:90px">Every homeowners association is different. Different sets of assets, different financials and different historical backgrounds that have brought you to the present. Each of these is taken into consideration to customize your 30 year budget and build the most accurate, most precise long-term savings (“reserve”) report you can buy.</p>
  <p class="service-text abs" style="left:303px">Your property represents a significant capital investment. In many cases, your business is dependent on the livelihood and functionality of the edifice in which it resides. We believe a fiscally sound plan and budget of capital expenses is as essential as the building itself. We are comprehensive, thorough and intense about our calculations.</p>
  <p class="service-text abs" style="left:515px;top:194px">Much like HOA’s and condominiums, you have finite funds that originate from a constituent base of tax payers. Planning the use of these funds and repairs and/or maintenance of public assets is essential to transparency and candid communication with your constituents. Being in control of the future starts with a financial plan.</p>

  <div class="more-btn abs" style="left:90px">MORE</div>
  <div class="more-btn abs" style="left:303px">MORE</div>
  <div class="more-btn abs" style="left:514px">MORE</div>
</section>

<section class="callback abs">
  <h2 class="callback-title abs">REQUEST CALL BACK.</h2>
  <p class="callback-text abs">Would you like to speak to one of our financial advisers over the phone? Just submit your details and we'll be in touch shortly. You can also email us if you would prefer.</p>
  <div class="field abs" style="left:262px;top:52px">how can we help?<span class="arrow">▼</span></div>
  <div class="field abs" style="left:436px;top:52px">you phone number*</div>
  <div class="field abs" style="left:262px;top:90px">You name*</div>
  <div class="field abs" style="left:436px;top:90px">you email</div>
  <div class="submit abs">SUBMIT
    <svg width="6" height="8" viewBox="0 0 6 8"><path d="M1 1l3 3-3 3" stroke="#fff" stroke-width="1.6" fill="none"/></svg>
  </div>
</section>

<footer class="site-footer abs">
  <div class="footer-brand abs"><span class="brand-dot"></span>Copper Ridge Capital</div>
  <div class="footer-info abs">
    Copper Ridge Capital, LLC<br>
    Serving Idaho, Montana, Oregon, Utah, Washington &amp; Wyoming<br>
    Phone:&nbsp;&nbsp;&nbsp;(208) 555-0142<br>
    E-mail:&nbsp;&nbsp;&nbsp;Dana@CopperRidgeCapital.example
  </div>
  <nav class="footer-nav abs">WHO WE ARE<br>SERVICES<br>CONTACT</nav>
  <div class="social abs"><span></span><span></span><span></span><span></span></div>
</footer>

<div class="copyright abs">Copyright © COPPER RIDGE CAPITAL 2019. All Rights Reserved</div>

</body>
</html>
```